Custom Software Company Needs a Direct Mail Postcard

We need a postcard or A5 sized mailer to be used in an unaddressed mail drop.
Headline: Warning
Subhead: Excel & Paper Considered Harmful For Business
Possible images: triangular warning logos
Breakout (possibly a sidebar):
Breakout Headline: Free Quotes
We come and discuss your requirements and provide a free, no obligation quote.
Main text:
- Are you juggling multiple systems that don't talk to each other?
- Are staff constantly updating or re-entering data?
- Do you worry that things will be missed?
- Do staff spend a lot of time doing the same thing over and over?
- Is finding information or reports challenging?
Custom software can bring all your information together in one place and automate all the repetitive tasks. With the information together, things are no longer missed and you can get the information you need, when you need it.
Whatever your requirements, we can build a system to suit. Visit our website or call us now for a free, no obligation quote.
Call 9371 5862
www.9 zu.com.au
Logo
Possible items to use on the postcard:
- Client logos
- Testimonials
- Picture of me
- Branding items on the website
Light industry manufacturers, heavy machinery hire, construction, occupational health and safety.
It Company

```html
<!DOCTYPE html>
<html lang="en">
<head>
<meta charset="utf-8">
<title>Warning – Custom Business Software Mailer</title>
<link rel="stylesheet" href="https://fonts.googleapis.com/css2?family=Lato:wght@400&family=Open+Sans:wght@400&family=EB+Garamond:wght@400&display=swap">
<style>
  :root {
    --brand-blue: #3d5f8c;
    --frame-blue: #8ea3c2;
    --soft-blue: #8aaad0;
    --mark-blue: #8fa5c9;
    --paper: #ffffff;
    --faint-line: #ececec;
  }
  html, body { margin: 0; padding: 0; overflow: hidden; background: var(--paper); }
  .mailer {
    position: relative; width: 846px; height: 1200px; overflow: hidden;
    background: var(--paper); color: var(--brand-blue);
    font-family: "Lato", sans-serif;
    border-left: 1px solid #c9d2de; border-top: 1px solid #c9d2de; box-sizing: border-box;
  }
  .shapes { position: absolute; left: 0; top: 0; }
  .headline {
    position: absolute; left: 0; width: 880px; top: 76px; margin: 0; text-align: center;
    font-family: "Open Sans", sans-serif; font-weight: 400; font-size: 68px; line-height: 1;
    letter-spacing: 1px;
  }
  .subhead {
    position: absolute; left: 0; width: 852px; top: 146px; margin: 0; text-align: center;
    font-family: "EB Garamond", serif; font-weight: 400; font-size: 29px; line-height: 1;
    letter-spacing: 2.4px;
  }
  .questions { position: absolute; left: 0; top: 0; margin: 0; padding: 0; list-style: none; }
  .questions li {
    position: absolute; left: 155px; width: 270px;
    font-size: 20.5px; line-height: 35px;
  }
  .questions li::before {
    content: ""; position: absolute; left: -32px; top: 15px;
    width: 6px; height: 6px; border-radius: 50%; background: var(--brand-blue);
  }
  .quote-button {
    position: absolute; left: 495px; top: 286px; width: 247px; height: 71px;
    display: flex; align-items: center; justify-content: center;
    font-family: "EB Garamond", serif; font-size: 32px; letter-spacing: 1px; color: var(--paper);
  }
  .quote-note {
    position: absolute; left: 496px; top: 388px; margin: 0;
    font-size: 17px; line-height: 49.4px;
  }
  .call {
    position: absolute; left: 522px; top: 596px; margin: 0;
    font-family: "Open Sans", sans-serif; font-size: 26px; line-height: 34px;
  }
  .call .call-label { color: var(--soft-blue); }
  .web {
    position: absolute; left: 534px; top: 641px; margin: 0;
    font-family: "Open Sans", sans-serif; font-size: 23px; line-height: 30px;
  }
  .band-copy {
    position: absolute; left: 88px; margin: 0; color: var(--paper);
    font-size: 22px; line-height: 35px;
  }
  .band-copy.intro { top: 830px; }
  .band-copy.offer { top: 1006px; }
  .brand-name {
    position: absolute; left: 80px; top: 1144px; margin: 0;
    font-size: 34px; line-height: 44px; color: var(--brand-blue);
  }
</style>
</head>
<body>
<div class="mailer">
  <svg class="shapes" width="846" height="1200" viewBox="0 0 846 1200" aria-hidden="true">
    <rect class="blue-band" x="75.5" y="695" width="699.5" height="436.6" fill="var(--brand-blue)"/>
    <polygon class="question-arrow" points="75.5,193.6 438.5,193.6 438.5,695 256.5,821 75.5,695"
             fill="var(--paper)" stroke="var(--frame-blue)" stroke-width="1.2"/>
    <rect class="quote-frame" x="452" y="253" width="323" height="334" rx="53"
          fill="var(--paper)" stroke="var(--frame-blue)" stroke-width="1.2"/>
    <rect class="quote-button-bg" x="495" y="286" width="247" height="71" rx="9" fill="var(--brand-blue)"/>
    <rect class="quote-note-box" x="480" y="381" width="270" height="169" fill="none" stroke="var(--faint-line)" stroke-width="1"/>
    <polygon class="warning-triangle" points="626,1132 699,1026 775,1132" fill="var(--paper)"/>
    <rect class="warning-bar" x="696" y="1065" width="6" height="48" rx="3" fill="var(--mark-blue)"/>
    <circle class="warning-dot" cx="699" cy="1124" r="3.5" fill="var(--mark-blue)"/>
  </svg>

  <h1 class="headline">WARNING</h1>
  <p class="subhead">Excel &amp; Paper Considered Harmful For Business</p>

  <ul class="questions">
    <li style="top:210px">Are you juggling multi-<br>ple systems that don't<br>talk to each other?</li>
    <li style="top:327px">&nbsp;Are staff constantly up-<br>dating or re-entering<br>data?</li>
    <li style="top:445px">Do you worry that<br>things will be missed?</li>
    <li style="top:528px">Do staff spend a lot of<br>time doing the same<br>thing over and over?</li>
    <li style="top:645px">Is finding information or<br>reports challenging?</li>
  </ul>

  <div class="quote-button">Free Quotes</div>
  <p class="quote-note">We come and discuss your<br>requirements and provide a<br>free, no obligation quote.</p>

  <p class="call"><span class="call-label">Call :</span>&nbsp; 9371 5862</p>
  <p class="web">www.9 zu.com.au</p>

  <p class="band-copy intro">Custom software can bring all your information together in one<br>place and automate all the repetitive tasks. With the information<br>together, things are no longer missed and you can get the infor-<br>mation you need, when you need it.</p>
  <p class="band-copy offer">Whatever your requirements, we can build a system to<br>suit. Visit our website or call us now for a free, no obliga-<br>tion quote.</p>

  <p class="brand-name">NineZu</p>
</div>
</body>
</html>
```